Bramble Oak Range Outfitters business card

I want business cards that support my new logo design. I want something very classy, cool, unusual, colorful, etc.

Font:
- Serpentine-Bold-Bold for "BRAMBLE OAK"
- BrowalliaUPC for "RANGE OUTFITTERS"

Colors (CMYK code):
- BLACK ....... 0; 0; 0; 100;
- ORANGE ... gradient from 0; 65; 97.5; 0 to 0; 39; 97.5; 0

My apologies, here is the contact info.

Dale Hurley

731-555-0192

d.dale.hurley@postvale.net

Somewhere please add:

FMA Certified Instructor

State of Tennessee Certified Handgun Instructor

```html
<!DOCTYPE html>
<html lang="en">
<head>
<meta charset="utf-8">
<title>Bramble Oak Range Outfitters – Business Card</title>
<link rel="stylesheet" href="https://fonts.googleapis.com/css2?family=Exo+2:wght@400;500;700&display=swap">
<style>
  :root {
    --page-bg: #ecebe8;
    --ink-dark: #1a1a1a;
    --panel-dark-top: #3b3b3b;
    --panel-dark-bottom: #0f0f0f;
    --panel-light-top: #ffffff;
    --panel-light-bottom: #d6d6d6;
    --orange-deep: #f35a06;
    --orange-light: #f59c07;
    --text-white: #ffffff;
    --text-grey: #d0d0d0;
  }
  * { margin: 0; padding: 0; box-sizing: border-box; }
  html, body {
    width: 1200px; height: 1085px; overflow: hidden;
    background: var(--page-bg);
  }
  body {
    display: flex; align-items: center; justify-content: center;
    font-family: "Exo 2", sans-serif;
  }
  .card {
    position: relative;
    width: 1000px; height: 571px;
    border-radius: 6px; overflow: hidden;
    box-shadow: 0 18px 40px rgba(0,0,0,.25);
  }
  .card__shapes { position: absolute; inset: 0; }

  .contact { position: absolute; right: 470px; text-align: right; white-space: nowrap;
    color: var(--ink-dark); font-size: 25px; line-height: 34px; letter-spacing: .5px; }
  .contact--phone { top: 103px; }
  .contact--email { top: 268px; }
  .contact--cert { top: 423px; }

  .brand {
    position: absolute; left: 620px; width: 360px; top: 100px;
    text-align: center; font-weight: 700;
    color: var(--orange-light);
  }
  .brand__mark {
    display: block; width: 22px; height: 22px; margin: 0 auto 18px;
    background: var(--orange-light);
  }
  .brand__name { font-size: 40px; letter-spacing: 2px; line-height: 1.05; }
  .brand__tag { font-size: 22px; letter-spacing: 3px; margin-top: 8px; }

  .person { position: absolute; left: 640px; top: 360px; width: 340px; color: var(--text-white); }
  .person__name { font-size: 36px; font-weight: 500; letter-spacing: 1.5px; }
  .person__title { font-size: 22px; line-height: 30px; color: var(--text-grey); margin-top: 8px; letter-spacing: .5px; }
</style>
</head>
<body>
  <div class="card">
    <svg class="card__shapes" viewBox="0 0 1000 571" width="1000" height="571">
      <defs>
        <linearGradient id="darkPanel" x1="0" y1="0" x2="0" y2="1">
          <stop offset="0" stop-color="#3b3b3b"/>
          <stop offset="1" stop-color="#0f0f0f"/>
        </linearGradient>
        <linearGradient id="lightPanel" x1="0" y1="0" x2="1" y2="1">
          <stop offset="0" stop-color="#ffffff"/>
          <stop offset="1" stop-color="#d6d6d6"/>
        </linearGradient>
        <linearGradient id="orangeRing" x1="0" y1="1" x2="1" y2="0">
          <stop offset="0" stop-color="#f35a06"/>
          <stop offset="1" stop-color="#f59c07"/>
        </linearGradient>
      </defs>
      <rect class="panel-dark" width="1000" height="571" fill="url(#darkPanel)"/>
      <path class="panel-light" fill="url(#lightPanel)"
        d="M0 0 H560 C560 40 600 70 600 120 C600 175 555 185 552 205
           C550 225 600 240 600 285 C600 335 552 345 552 365
           C552 385 600 395 600 440 C600 495 560 520 560 571 H0 Z"/>
      <g class="icon icon--phone" fill="none" stroke="url(#orangeRing)" stroke-width="3">
        <circle cx="565" cy="120" r="22"/>
        <path d="M556 110 q-2 6 4 13 q6 7 13 6 l2-5 -6-4 -3 3 q-4-2-7-7 l3-3 -3-6z" stroke-linejoin="round"/>
      </g>
      <g class="icon icon--mail" fill="none" stroke="url(#orangeRing)" stroke-width="3" stroke-linejoin="round">
        <circle cx="565" cy="285" r="22"/>
        <rect x="554" y="277" width="22" height="16" rx="2"/>
        <path d="M554 278 l11 9 11-9"/>
      </g>
      <g class="icon icon--tick" fill="none" stroke="url(#orangeRing)" stroke-width="3" stroke-linecap="round" stroke-linejoin="round">
        <circle cx="565" cy="440" r="22"/>
        <path d="M555 441 l7 7 13-14"/>
      </g>
    </svg>

    <div class="contact contact--phone">731-555-0192</div>
    <div class="contact contact--email">d.dale.hurley@postvale.net</div>
    <div class="contact contact--cert">FMA Certified Instructor</div>

    <div class="brand">
      <span class="brand__mark"></span>
      <div class="brand__name">BRAMBLE OAK</div>
      <div class="brand__tag">RANGE OUTFITTERS</div>
    </div>

    <div class="person">
      <div class="person__name">DALE HURLEY</div>
      <div class="person__title">State of Tennessee Certified<br>Handgun Instructor</div>
    </div>
  </div>
</body>
</html>
```